Product Menu 8 x 11- Home Inspection Company Ancillary Services

Hello, on the front side of the flyer will be all about sewer camera inspections. These will include the images of the damages on the front and the information on the Sewer Scope Inspections: Safeguard Your Home from Hidden Plumbing Issues.
On the back will include indoor air quality. Solar Panel Inspections, Roof Certifications, and Expert Raised Foundation Review.
Please use logo and colors as a branding guide for the flyer.
$275- Sewer Camera Fee
$495 -Indoor Air Quality Inspection- Getting an indoor air quality (IAQ) inspection for mold when buying a home is crucial for health, safety, and financial protection. Mold can cause serious respiratory issues, especially for those with allergies or asthma, and toxic molds like black mold pose additional risks. It often grows in hidden areas, such as behind walls or in HVAC systems, often linked to water damage or structural issues. Early detection allows you to negotiate remediation costs, prevent mold from spreading, and avoid expensive repairs, ensuring a safe and sound investment.
$395 -Solar Panel Inspection- Getting a solar panel inspection when buying a home is essential to ensure efficiency, safety, and long-term savings. It verifies the system’s condition, identifying issues like damaged panels, faulty wiring, or inefficient inverters that could impact performance or pose safety risks. The inspection also evaluates the system’s energy output and compatibility with your energy needs, ensuring you’re benefiting from the investment. Additionally, understanding the age, warranty, and maintenance history of the system helps avoid unexpected repair costs and maximizes the value of this eco-friendly feature.
$399 Roof Certifications- Obtaining a roof certification when buying a home is vital for assessing the roof's condition, lifespan, and potential repair needs. This certification provides a professional evaluation, ensuring the roof is free from leaks, damage, or structural issues, which could lead to costly repairs. Many insurance companies require a roof certification before issuing or renewing a policy, particularly for older roofs, to confirm it meets safety standards. Having this certification not only provides peace of mind but also helps facilitate insurance coverage and protects your investment in the property.
$199- Advanced Foundation Review-An advanced foundation review by a licensed foundation contractor is essential when buying a home, as it provides a detailed assessment beyond what a general home inspector can offer. While home inspectors are trained generalists who identify visible issues, a foundation contractor is a specialist with the expertise to evaluate structural integrity, detect hidden problems, and determine the severity of any concerns. This specialized review can uncover issues like uneven settling, cracks, or drainage problems that may require repairs, ensuring you have a clear understanding of the foundation's condition before making a significant investment.
Real Estate Buyers and Real Estate Agents

```html
<!DOCTYPE html>
<html lang="en">
<head>
<meta charset="utf-8">
<title>Keystone Group – Sewer Scope &amp; Additional Services Flyer</title>
<link rel="stylesheet" href="https://fonts.googleapis.com/css2?family=Oswald:wght@400;500;600&family=Roboto+Condensed:wght@400;700&family=Roboto:wght@400;700;900&family=Lobster&display=swap">
<style>
:root{
  --blue:#1c63b4;
  --blue-dark:#154e91;
  --red:#d9323b;
  --ink:#1e2733;
  --white:#ffffff;
  --stage:#d7d7d7;
}
*{box-sizing:border-box;margin:0;padding:0}
html,body{width:1200px;height:1200px;overflow:hidden}
body{background:var(--stage);font-family:"Roboto",Arial,sans-serif;color:var(--ink);position:relative}
.page{position:absolute;top:251px;width:551px;height:710px;background:var(--white);overflow:hidden}
.page--services{left:37px}
.page--sewer{left:615px}
.abs{position:absolute}
.photo{position:absolute}

/* brand */
.brand{position:absolute;display:flex;flex-direction:column;align-items:center;gap:5px}
.brand__dot{width:44px;height:44px;border-radius:50%;background:var(--blue)}
.brand__name{font-family:"Oswald",sans-serif;font-weight:600;color:var(--blue);font-size:12px;letter-spacing:.4px;white-space:nowrap}

/* services page */
.services-title{left:208px;top:0;width:343px;height:55px;background:var(--blue);clip-path:polygon(22px 0,100% 0,100% 100%,0 100%);
  color:var(--white);font-family:"Oswald",sans-serif;font-size:30px;font-weight:400;display:flex;align-items:center;justify-content:center;letter-spacing:.5px}
.hero-photo{left:0;top:0;width:232px;height:150px;border-bottom-right-radius:150px 130px;border-right:4px solid var(--red);border-bottom:4px solid var(--red);
  background:linear-gradient(160deg,#cfe0ef 0%,#b9cde0 45%,#5a6f84 100%)}
.fee-tag{left:372px;top:72px;width:179px;height:52px;background:var(--red);color:var(--white);text-align:center;clip-path:polygon(14px 0,100% 0,100% 100%,0 100%)}
.fee-tag__price{font-family:"Roboto",sans-serif;font-weight:900;font-size:25px;line-height:28px;margin-top:3px}
.fee-tag__label{font-family:"Oswald",sans-serif;font-size:13px;letter-spacing:.3px}

.svc-head{height:21px;background:var(--blue);color:var(--white);font-family:"Oswald",sans-serif;font-weight:500;font-size:13.5px;display:flex;align-items:center;padding-left:8px;letter-spacing:.2px}
.svc-head--left{left:0;width:282px;clip-path:polygon(0 0,100% 0,calc(100% - 14px) 100%,0 100%)}
.svc-head--right{left:284px;width:267px;padding-left:20px;clip-path:polygon(14px 0,100% 0,100% 100%,0 100%)}
.svc-head--right.center{justify-content:center;padding-left:14px}

.svc-text{font-family:"Roboto Condensed",sans-serif;font-size:8.7px;line-height:10.5px;text-align:justify;color:var(--ink)}
.svc-text p+p{margin-top:9px}
.svc-photo{width:86px;border-radius:4px}
.price-chip{position:absolute;background:var(--red);color:var(--white);font-weight:900;font-size:17px;width:86px;height:26px;display:flex;align-items:center;justify-content:center;border-radius:0 0 4px 4px}
.icon{position:absolute;width:36px;height:36px}
.divider{left:10px;top:398px;width:531px;height:2px;background:var(--blue)}

.footer-cta{left:0;top:666px;width:232px;height:44px;background:var(--red);clip-path:polygon(0 0,100% 0,calc(100% - 20px) 100%,0 100%);
  color:var(--white);font-family:"Lobster",cursive;font-size:15px;display:flex;align-items:center;padding-left:12px}
.footer-contact{left:232px;top:645px;width:319px;height:65px;background:var(--blue);clip-path:polygon(30px 0,100% 0,100% 100%,0 100%);
  color:var(--white);font-size:12.5px;line-height:15px;padding:13px 0 0 20px}

/* sewer page */
.sewer-block{left:239px;top:0;width:312px;height:356px;background:var(--blue)}
.sewer-title{left:239px;top:8px;width:312px;text-align:center;color:var(--white);font-family:"Oswald",sans-serif;font-size:44px;line-height:50px;font-weight:400}
.sewer-sub-band{left:262px;top:63px;width:266px;height:40px;background:var(--red);color:var(--white);font-family:"Oswald",sans-serif;font-size:29px;display:flex;align-items:center;justify-content:center}
.sewer-tagline{left:239px;top:109px;width:312px;text-align:center;color:var(--white);font-weight:700;font-size:12.8px;line-height:16px}
.damage-grid{left:322px;top:160px;width:212px;height:182px;display:grid;grid-template-columns:1fr 1fr;gap:5px}
.damage-grid div{border-radius:3px}
.tech-photo{left:84px;top:98px;width:155px;height:262px;background:linear-gradient(170deg,#7d8d6a 0%,#9aa186 35%,#4d4f52 70%,#cbcbc6 100%)}
.what-circle{left:-6px;top:200px;width:170px;height:170px;border-radius:50%;background:var(--blue);border:5px solid var(--white);box-shadow:0 0 0 4px var(--red);
  color:var(--white);padding:28px 16px 0 22px}
.what-circle h3{font-family:"Roboto",sans-serif;font-size:10.8px;line-height:12px;font-weight:700;margin-bottom:3px}
.what-circle p{font-size:8.2px;line-height:9.8px}
.why-band{left:150px;top:357px;width:401px;height:30px;background:var(--red);color:var(--white);font-family:"Roboto",sans-serif;font-weight:700;font-size:12.2px;
  display:flex;align-items:center;justify-content:flex-end;padding-right:12px;clip-path:polygon(20px 0,100% 0,100% 100%,0 100%)}
.benefit{position:absolute;width:250px}
.benefit h4{font-family:"Roboto",sans-serif;font-weight:700;color:var(--blue);font-size:11.5px;line-height:14px;padding-left:42px}
.benefit p{font-size:9.4px;line-height:11.8px;padding-left:42px;color:var(--ink)}
.benefit svg{position:absolute;left:4px;top:0;width:30px;height:30px}
.seal{position:absolute;width:56px;height:56px;border-radius:50%;top:584px}
</style>
</head>
<body>

<!-- ADDITIONAL SERVICES PAGE -->
<section class="page page--services">
  <div class="photo hero-photo" role="img" aria-label="Inspector in a hard hat with a clipboard pointing in front of a white two-storey house"></div>
  <h1 class="abs services-title">★ ADDITIONAL SERVICES ★</h1>
  <div class="brand" style="left:258px;top:62px;width:106px"><span class="brand__dot"></span><span class="brand__name">KEYSTONE GROUP</span></div>
  <div class="abs fee-tag"><div class="fee-tag__price">$275</div><div class="fee-tag__label">SEWER CAMERA</div></div>

  <h2 class="abs svc-head svc-head--left" style="top:153px">INDOOR AIR QUALITY INSPECTION</h2>
  <h2 class="abs svc-head svc-head--right" style="top:153px">ROOF INSPECTION &amp; CERTIFICATION</h2>

  <svg class="icon" style="left:32px;top:184px" viewBox="0 0 36 36" fill="none" stroke="#1c63b4" stroke-width="2.2"><path d="M4 17 18 5l14 12M8 14v18h20V14"/><path d="M12 20c2-2 4 2 6 0s4 2 6 0M12 25c2-2 4 2 6 0s4 2 6 0"/></svg>
  <div class="photo svc-photo" style="left:12px;top:240px;height:134px;background:linear-gradient(160deg,#6d737c,#2f343b 60%,#4f8e70)" role="img" aria-label="Inspector using an air quality testing device"></div>
  <div class="price-chip" style="left:12px;top:374px">$495</div>
  <div class="abs svc-text" style="left:104px;top:186px;width:160px">
    <p>Getting an indoor air quality (IAQ) inspection for mold when buying a home is crucial for health, safety, and financial protection. Mold can cause serious respiratory issues, especially for those with allergies or asthma and toxic molds like black mold pose additional risks. It often grows in hidden areas, such as behind walls or in HVAC systems, often linked to water damage or structural issues.</p>
    <p>Early detection allows you to negotiate remediation costs, prevent mold from spreading, and avoid expensive repairs, ensuring a safe and sound investment.</p>
  </div>

  <svg class="icon" style="left:484px;top:184px;width:44px" viewBox="0 0 44 36" fill="none" stroke="#1c63b4" stroke-width="2.2"><path d="M2 22 22 6l20 16M8 18v14h28V18"/><path d="M12 15h20M10 19h24"/></svg>
  <div class="photo svc-photo" style="left:451px;top:240px;height:134px;background:linear-gradient(170deg,#9ec0e0,#4d6a88 55%,#2c3440)" role="img" aria-label="Inspector checking a shingle roof"></div>
  <div class="price-chip" style="left:451px;top:374px">$399</div>
  <div class="abs svc-text" style="left:289px;top:180px;width:152px">
    <p>Obtaining a roof certification when buying a home is vital for assessing the roof's condition, lifespan, and potential repair needs. This certification provides a professional evaluation, ensuring the roof is free from leaks, damage, or structural issues, which could lead to costly repairs. Many insurance companies require a roof certification before issuing or renewing a policy, particularly for older roofs, to confirm it meets safety standards.</p>
    <p>Having this certification not only provides peace of mind but also helps facilitate insurance coverage and protects your investment in the property.</p>
  </div>

  <div class="abs divider"></div>

  <h2 class="abs svc-head svc-head--left" style="top:410px">RAISED FOUNDATION REVIEW</h2>
  <h2 class="abs svc-head svc-head--right center" style="top:410px;padding-left:60px">SOLAR PANEL INSPECTION</h2>

  <svg class="icon" style="left:32px;top:440px" viewBox="0 0 36 36" fill="none" stroke="#1c63b4" stroke-width="2.2"><path d="M8 14 20 4l12 10M12 11v12h16V11"/><path d="M2 26h8l6 4h8l8-6M2 33h10"/></svg>
  <div class="photo svc-photo" style="left:12px;top:493px;height:110px;background:linear-gradient(150deg,#3a2a20,#8a6a4c 55%,#2a211b)" role="img" aria-label="Crawl space under a raised foundation"></div>
  <div class="price-chip" style="left:12px;top:600px">$199</div>
  <div class="abs svc-text" style="left:104px;top:440px;width:160px">
    <p>An advanced foundation review by a licensed foundation contractor is essential when buying a home, as it provides a detailed assessment beyond what a general home inspector can offer. While home inspectors are trained generalists who identify visible issues, a foundation contractor is a specialist with the expertise to evaluate structural integrity, detect hidden problems, and determine the severity of any concerns. This specialized review can uncover issues like uneven settling, cracks, or drainage problems that may require repairs, ensuring you have a clear understanding of the foundation's condition before making a significant investment.</p>
  </div>

  <svg class="icon" style="left:478px;top:438px;width:40px;height:40px" viewBox="0 0 40 40" fill="none" stroke="#1c63b4" stroke-width="2"><circle cx="20" cy="7" r="4"/><path d="M8 16h24l4 14H4z M12 16l-2 14M20 16v14M28 16l2 14M6 23h28M20 30v8M14 38h12"/></svg>
  <div class="photo svc-photo" style="left:451px;top:493px;height:110px;background:linear-gradient(165deg,#8fb7de,#cfa88a 55%,#3d6d9a)" role="img" aria-label="House roof with solar panels beside a pool"></div>
  <div class="price-chip" style="left:451px;top:600px">$395</div>
  <div class="abs svc-text" style="left:289px;top:440px;width:152px">
    <p>Getting a solar panel inspection when buying a home is essential to ensure efficiency, safety, and long-term savings. It verifies the system's condition, identifying issues like damaged panels, faulty wiring, or inefficient inverters that could impact performance or pose safety risks. The inspection also evaluates the system's energy output and compatibility with your energy needs, ensuring you're benefiting from the investment. Additionally, understanding the age, warranty, and maintenance history of the system helps avoid unexpected repair costs and maximizes the value of this eco-friendly feature.</p>
  </div>

  <div class="abs footer-cta">Schedule My Inspection Today!</div>
  <div class="abs footer-contact">(800) 555-0142<br>hello@keystoneinspect.com<br>KEYSTONEINSPECT.COM</div>
</section>

<!-- SEWER SCOPE PAGE -->
<section class="page page--sewer">
  <div class="abs sewer-block"></div>
  <div class="brand" style="left:10px;top:12px;width:110px"><span class="brand__dot" style="width:52px;height:52px"></span><span class="brand__name">KEYSTONE GROUP</span></div>
  <div class="photo tech-photo" role="img" aria-label="Technician feeding a sewer camera reel into a cleanout pipe"></div>
  <h1 class="abs sewer-title">SEWER SCOPE</h1>
  <div class="abs sewer-sub-band">★ INSPECTIONS ★</div>
  <p class="abs sewer-tagline">SAFEGUARD YOUR HOME<br>FROM HIDDEN PLUMBING&nbsp; ISSUES</p>
  <div class="abs damage-grid">
    <div style="background:radial-gradient(circle,#3a3a38 15%,#9a9a94 60%,#d4d0c4)" role="img" aria-label="Camera view inside a clean sewer pipe"></div>
    <div style="background:radial-gradient(circle,#5a3a24 20%,#a77a55 60%,#6a4a30)" role="img" aria-label="Camera view of rust buildup in a pipe"></div>
    <div style="background:radial-gradient(circle,#2a2620 15%,#9c8a55 55%,#514838)" role="img" aria-label="Camera view of a cracked pipe joint"></div>
    <div style="background:radial-gradient(circle,#1a2a4a 15%,#6d7fa8 55%,#a29070)" role="img" aria-label="Camera view of tree root intrusion in a pipe"></div>
  </div>
  <div class="abs what-circle">
    <h3>WHAT IS A SEWER<br>SCOPE INSPECTION?</h3>
    <p>A sewer scope inspection uses a camera to inspect your home's sewer lines. The camera is inserted into the sewer pipe, allowing an inspector to detect blockages, cracks, tree root intrusions, and other issues that can cause significant damage if left unaddressed</p>
  </div>
  <div class="abs why-band">WHY YOU SHOULD GET A SEWER SCOPE INSPECTION?</div>

  <div class="benefit" style="left:10px;top:404px">
    <svg viewBox="0 0 30 30"><rect x="3" y="5" width="24" height="16" rx="2" fill="#1c63b4"/><circle cx="15" cy="13" r="4" fill="#fff"/><path d="M10 25h10" stroke="#d9323b" stroke-width="3"/></svg>
    <h4>PREVENT COSTLY REPAIRS</h4>
    <p>Sewer line issues can be extremely expensive to fix, with some repairs costing thousands of dollars. A sewer scope inspection can identify problems early, potentially saving you from dealing with costly repairs down the road.</p>
  </div>
  <div class="benefit" style="left:10px;top:490px">
    <svg viewBox="0 0 30 30"><path d="M10 10 18 3l8 7v8H10z" fill="#d9323b"/><path d="M2 20h7l5 3h7l7-5-2-2-6 3h-6" fill="none" stroke="#1c63b4" stroke-width="2.5"/></svg>
    <h4>PROTECT YOUR INVESTMENT</h4>
    <p>Whether you're buying or selling a home, understanding the condition of the sewer system can impact your decision. For buyers, it helps avoid unexpected expenses. For sellers, it can provide peace of mind and ensure the sale goes smoothly.</p>
  </div>
  <div class="benefit" style="left:10px;top:580px">
    <svg viewBox="0 0 30 30"><path d="M15 3 28 27H2z" fill="none" stroke="#d9323b" stroke-width="2.5"/><path d="M15 11v8" stroke="#1c63b4" stroke-width="3"/><circle cx="15" cy="23" r="1.7" fill="#1c63b4"/></svg>
    <h4>CATCH HIDDEN PROBLEMS</h4>
    <p>Sewer line issues often remain hidden until it's too late. Without a sewer scope inspection, it's nearly impossible to identify problems that could lead to sewage backups, unpleasant odors, and costly damages.</p>
  </div>
  <div class="benefit" style="left:283px;top:404px;width:262px">
    <svg viewBox="0 0 30 30"><path d="M15 2 28 15 15 28 2 15z" fill="#d9323b"/><path d="M15 7 23 15 15 23 7 15z" fill="#fff"/><circle cx="15" cy="15" r="3" fill="#1c63b4"/></svg>
    <h4>AVOID HEALTH HAZARDS</h4>
    <p>Faulty sewer systems can lead to sewage backups, which are not only unpleasant but also pose serious health risks. Inspections help ensure your home's plumbing is functioning safely</p>
  </div>
  <div class="benefit" style="left:283px;top:490px;width:262px">
    <svg viewBox="0 0 30 30"><path d="M3 6h14v8H9v4H3z" fill="#1c63b4"/><path d="M2 22c3-2 5 2 8 0s5 2 8 0 5 2 8 0M2 27c3-2 5 2 8 0s5 2 8 0 5 2 8 0" fill="none" stroke="#1c63b4" stroke-width="2"/></svg>
    <h4>ENSURE PROPER FUNCTIONING</h4>
    <p>A sewer scope inspection gives you a better understanding of how well your sewer system is functioning. It helps detect potential issues like blockages from tree roots, misaligned pipes, or wear and tear that&nbsp; may cause drainage problems</p>
  </div>

  <div class="seal" style="left:322px;background:radial-gradient(circle,#fff 45%,#1c63b4 47%,#1c63b4 70%,#d9323b 72%)"></div>
  <div class="seal" style="left:385px;background:radial-gradient(circle,#2b4a7a 45%,#c9a23f 47%,#e4c766 80%,#9b7a25 82%)"></div>
  <div class="seal" style="left:448px;background:radial-gradient(circle,#2b2b2b 45%,#b08a3a 47%,#d6b767 80%,#7a5e20 82%)"></div>

  <div class="abs footer-cta">Schedule My Inspection Today!</div>
  <div class="abs footer-contact">(800) 555-0142<br>hello@keystoneinspect.com<br>KEYSTONEINSPECT.COM</div>
</section>

</body>
</html>
```